Yoga Instrucor

I need my personal business cards, i would like the front a kind of light but vibrant red and matt gold.

Industry/Entity Type

Business

Contact Information for Business Card

Cordelia Hastrup
Yoga Instructor
RYT 200, BROKU (NYC) Yoga RYT 500,
CPR/ AED Certified,
hastrupcordelia@quillbox.com
512 604 8893
Adult Yoga, Private Yoga, Group Classes, Restorative, Meditation, Child Yoga.

```html
<!DOCTYPE html>
<html lang="en">
<head>
<meta charset="utf-8">
<title>Cordelia Hastrup – Yoga Instructor Business Cards</title>
<link rel="stylesheet" href="https://fonts.googleapis.com/css2?family=Gentium+Book+Plus&display=swap">
<style>
  :root {
    --page: #ffffff;
    --red: #ff0000;
    --gold-dark: #9a3a00;
    --gold-mid: #c97a25;
    --gold-light: #f5b24a;
    --gold-edge: #7a4a00;
    --gold-shine: #f2e04a;
    --ink-light: #ffffff;
    --ink-dark: #2a0000;
    --lotus-a: #f0b070;
    --lotus-b: #b0651e;
  }
  * { margin: 0; padding: 0; box-sizing: border-box; }
  html, body { width: 988px; height: 1200px; overflow: hidden; background: var(--page); }
  body { position: relative; font-family: "Gentium Book Plus", Georgia, serif; color: var(--ink-light); }

  .card {
    position: absolute;
    width: 795px;
    height: 492px;
    background: var(--red);
    box-shadow: 0 8px 28px rgba(0,0,0,0.28);
    overflow: hidden;
  }
  .card--front { left: 98px; top: 90px; }
  .card--back  { left: 95px; top: 624px; }

  .gold-band {
    position: absolute;
    top: 0;
    width: 99px;
    height: 100%;
    background: linear-gradient(to bottom, var(--gold-dark) 0%, var(--gold-mid) 30%, var(--gold-light) 50%, var(--gold-mid) 70%, var(--gold-dark) 100%);
  }
  .gold-band::after {
    content: "";
    position: absolute;
    top: 0;
    width: 14px;
    height: 100%;
    background: linear-gradient(to bottom, var(--gold-edge) 0%, #c8a030 35%, var(--gold-shine) 50%, #c8a030 65%, var(--gold-edge) 100%);
  }
  .gold-band--left { left: 0; }
  .gold-band--left::after { right: 0; border-right: 3px solid var(--gold-edge); }
  .gold-band--right { right: 0; }
  .gold-band--right::after { left: 0; border-left: 3px solid var(--gold-edge); }

  .lotus-mark {
    position: absolute;
    left: 222px;
    top: 69px;
    width: 355px;
    height: 239px;
  }

  .services {
    position: absolute;
    left: 99px;
    right: 99px;
    text-align: center;
    font-size: 28px;
    letter-spacing: 0.2px;
    white-space: nowrap;
  }
  .services--row1 { top: 370px; }
  .services--row2 { top: 429px; }

  .centered { position: absolute; left: 99px; right: 99px; text-align: center; white-space: nowrap; }
  .name { top: 62px; font-size: 38px; }
  .role { top: 118px; font-size: 27px; }
  .credential { font-size: 18px; color: var(--ink-dark); }
  .credential--1 { top: 193px; }
  .credential--2 { top: 232px; }
  .credential--3 { top: 271px; }
  .contact { font-size: 25px; display: flex; justify-content: center; align-items: center; gap: 8px; }
  .contact svg { flex: none; }
  .contact--phone { top: 350px; }
  .contact--email { top: 404px; }
</style>
</head>
<body>
  <section class="card card--front">
    <div class="gold-band gold-band--left"></div>
    <div class="gold-band gold-band--right"></div>
    <svg class="lotus-mark" role="img" aria-label="Gold lotus flower illustration with a vertical column of chakra-coloured dots" viewBox="0 0 355 239">
      <defs>
        <radialGradient id="lotusGlow" cx="50%" cy="60%" r="60%">
          <stop offset="0%" stop-color="var(--lotus-a)"/>
          <stop offset="100%" stop-color="var(--lotus-b)" stop-opacity="0"/>
        </radialGradient>
      </defs>
      <ellipse cx="177" cy="130" rx="177" ry="110" fill="url(#lotusGlow)"/>
    </svg>
    <p class="services services--row1">Adult Yoga • Private Yoga • Group Classes</p>
    <p class="services services--row2">Restorative • Meditation • Child Yoga</p>
  </section>

  <section class="card card--back">
    <div class="gold-band gold-band--left"></div>
    <div class="gold-band gold-band--right"></div>
    <h1 class="centered name" style="font-weight:400">Cordelia Hastrup</h1>
    <p class="centered role">Yoga Instructor</p>
    <p class="centered credential credential--1">RYT 200,</p>
    <p class="centered credential credential--2">BROKU (NYC) Yoga RYT 500,</p>
    <p class="centered credential credential--3">CPR/ AED Certified</p>
    <p class="centered contact contact--phone">
      <svg width="20" height="24" viewBox="0 0 20 24" aria-hidden="true"><path d="M5 1 L8 7 L6 9 C7 13 9 16 12 18 L14 16 L19 19 L17 23 C9 22 2 14 1 5 Z" fill="none" stroke="var(--ink-light)" stroke-width="2" stroke-linejoin="round"/></svg>
      <span>512 604 8893</span>
    </p>
    <p class="centered contact contact--email">
      <svg width="22" height="16" viewBox="0 0 22 16" aria-hidden="true"><rect x="1" y="1" width="20" height="14" fill="none" stroke="var(--ink-light)" stroke-width="1.6"/><path d="M1 1 L11 9 L21 1" fill="none" stroke="var(--ink-light)" stroke-width="1.6"/></svg>
      <span>hastrupcordelia@quillbox.com</span>
    </p>
  </section>
</body>
</html>
```